Business Cards

We were billed for this because the project timed out. Please give me another designed to open this back up. I was not happy with the last designs (that I was charged for).
we are also using the logo with Clear Water Care, Season After Season
Also want to utilize Caring for Every Pool Like It Were Ours.

Contact Information for Business Card

Marlowe Stone Group Inc

```html
<!DOCTYPE html>
<html lang="en">
<head>
<meta charset="utf-8">
<title>Marlowe Stone Group – Business Cards</title>
<link href="https://fonts.googleapis.com/css2?family=Arimo:wght@400;700&display=swap" rel="stylesheet">
<style>
  :root {
    --backdrop: #3d3d3d;
    --card-white: #ffffff;
    --brand-blue: #1469b6;
    --brand-blue-deep: #0b4586;
    --accent-cyan: #3fc3e8;
    --ink-dark: #333333;
    --ink-grey: #777777;
    --strip-grey: #3a3a3a;
    --rule: #cfcfcf;
  }
  * { box-sizing: border-box; margin: 0; padding: 0; }
  html, body {
    width: 1200px; height: 803px; overflow: hidden;
    background: var(--backdrop);
    font-family: "Arimo", Arial, sans-serif;
  }
  .stage {
    width: 1200px; height: 803px;
    display: flex; align-items: center; justify-content: center; gap: 40px;
  }
  .card {
    position: relative; width: 540px; height: 310px;
    border-radius: 18px; overflow: hidden;
  }
  .brand-name {
    display: flex; align-items: center; gap: 10px; white-space: nowrap;
    font-weight: 700; letter-spacing: 1px;
  }
  .brand-mark { flex: none; }
  .brand-tagline {
    white-space: nowrap; text-transform: uppercase; letter-spacing: 2px;
  }

  /* Front */
  .card-front { background: var(--card-white); }
  .card-front .bands { position: absolute; inset: 0; }
  .brand-front { position: absolute; right: 46px; top: 52px; }
  .brand-front .brand-name { font-size: 22px; color: var(--ink-dark); }
  .brand-front .brand-mark { width: 18px; height: 18px; background: var(--brand-blue); }
  .brand-front .brand-tagline {
    margin-top: 5px; margin-left: 28px; font-size: 9.5px; color: var(--ink-dark);
  }
  .divider {
    position: absolute; left: 30px; right: 30px; top: 146px;
    height: 1px; background: var(--rule);
  }
  .person { position: absolute; left: 34px; top: 166px; }
  .person-name { font-weight: 700; font-size: 19px; color: var(--brand-blue); letter-spacing: .5px; white-space: nowrap; }
  .person-title { font-size: 12px; color: var(--ink-grey); margin-top: 2px; }
  .contacts { list-style: none; position: absolute; left: 34px; top: 211px; }
  .contacts li {
    display: flex; align-items: center; gap: 8px; white-space: nowrap;
    font-size: 12.5px; color: var(--ink-dark); line-height: 17px;
  }
  .contacts svg { width: 11px; height: 11px; fill: var(--brand-blue); flex: none; }
  .address {
    position: absolute; right: 34px; top: 168px; text-align: right;
    font-size: 12.5px; line-height: 18px; color: var(--ink-dark); white-space: nowrap;
  }
  .website {
    position: absolute; right: 30px; bottom: 20px;
    font-size: 13px; color: var(--card-white); letter-spacing: .3px; white-space: nowrap;
  }

  /* Back */
  .card-back {
    background: var(--brand-blue);
    display: flex; flex-direction: column; align-items: center; justify-content: center;
  }
  .brand-back .brand-name { color: var(--accent-cyan); font-size: 26px; }
  .brand-back .brand-mark { background: var(--accent-cyan); width: 20px; height: 20px; }
  .brand-back .brand-tagline {
    margin-top: 5px; margin-left: 30px; font-size: 10.5px; color: var(--brand-blue-deep);
  }
  .commitment {
    margin-top: 58px; font-size: 15px; color: var(--card-white); letter-spacing: .3px; white-space: nowrap;
  }
</style>
</head>
<body>
<main class="stage">
  <section class="card card-front" aria-label="Business card front">
    <svg class="bands" viewBox="0 0 540 310" aria-hidden="true">
      <rect x="0" y="276" width="340" height="12" fill="var(--strip-grey)"/>
      <path d="M0,288 L322,288 Q330,288 332,280 L336,262 Q338,252 348,252 L540,252 L540,310 L0,310 Z" fill="var(--brand-blue)"/>
    </svg>

    <div class="brand brand-front">
      <div class="brand-name"><span class="brand-mark"></span>MARLOWE STONE GROUP</div>
      <div class="brand-tagline">Clear Water Care, Season After Season</div>
    </div>

    <div class="divider"></div>

    <div class="person">
      <div class="person-name">DANA WHITFIELD</div>
      <div class="person-title">President</div>
    </div>

    <ul class="contacts">
      <li><svg viewBox="0 0 24 24"><path d="M6.6 10.8a15.1 15.1 0 0 0 6.6 6.6l2.2-2.2a1 1 0 0 1 1-.25 11.4 11.4 0 0 0 3.6.57 1 1 0 0 1 1 1V20a1 1 0 0 1-1 1A17 17 0 0 1 3 4a1 1 0 0 1 1-1h3.5a1 1 0 0 1 1 1c0 1.25.2 2.45.57 3.57a1 1 0 0 1-.25 1z"/></svg>555-214-7730</li>
      <li><svg viewBox="0 0 24 24"><path d="M3 3h18v18H3z M5 5v14h14V5z" fill-rule="evenodd"/></svg>555-219-4086</li>
      <li><svg viewBox="0 0 24 24"><path d="M2 5h20v14H2z M4 7v.5l8 5 8-5V7z" fill-rule="evenodd"/></svg>info@marlowestonegroup.com</li>
    </ul>

    <div class="address">412 Fernbrook Lane<br>Halden, Canada 20519</div>

    <div class="website">www.marlowestonegroup.com</div>
  </section>

  <section class="card card-back" aria-label="Business card back">
    <div class="brand brand-back">
      <div class="brand-name"><span class="brand-mark"></span>MARLOWE STONE GROUP</div>
      <div class="brand-tagline">Clear Water Care, Season After Season</div>
    </div>
    <p class="commitment">Caring for Every Pool Like It Were Ours</p>
  </section>
</main>
</body>
</html>
```